Profesional personal website needs design and business card

I need a business card with my professional name as a logo "Marlo Vitality" for my business. I am a Wellness Coach, consultant and trainer. So it should be professional, wellness oriented and modern.

Target Market(s)

Private clients, governments, corporations. Luxury and high market.

Industry/Entity Type

Health And Wellness

Contact Information for Business Card

Marlo Vitality should be the logo

Colors

Designer to choose colors to be used in the design.

Requirements
Must have
• Marlo Vitality
• Name: Tomás Arribal
• Wellness Coach, Consultant & Trainer.
• Website: www.marlovitality.example
• Phone:
• Spain (+34) 612 480 397
• (USA) +1 (555) 318 2046
Nice to have
• The most important is the design of "Marlo Vitality", as this is going to be my personal brand logo. It should be professional, wellness, high end and actual.
Should not have
• no golds, no baroque style..

```html
<!DOCTYPE html>
<html lang="en">
<head>
<meta charset="utf-8">
<title>Marlo Vitality — Business Card</title>
<link href="https://fonts.googleapis.com/css2?family=Montserrat:wght@700&family=Lato:wght@400&display=swap" rel="stylesheet">
<style>
  :root {
    --brand-blue: #1172bd;
    --paper: #ffffff;
    --backdrop: #2b2b2d;
    --text-grey: #4a4a4a;
    --rule-blue: #1172bd;
  }
  * { box-sizing: border-box; margin: 0; padding: 0; }
  html, body { width: 1200px; height: 900px; overflow: hidden; }
  body {
    background: var(--backdrop);
    font-family: 'Lato', sans-serif;
    display: flex;
    flex-direction: column;
    align-items: center;
    justify-content: center;
    gap: 34px;
  }
  .card {
    width: 700px;
    height: 400px;
    border-radius: 26px;
    position: relative;
    overflow: hidden;
  }
  /* Front */
  .card-front {
    background: var(--brand-blue);
    color: var(--paper);
    display: flex;
    flex-direction: column;
    align-items: center;
    justify-content: center;
    gap: 26px;
  }
  .brand-lockup {
    display: flex;
    align-items: center;
    gap: 16px;
  }
  .brand-dot {
    width: 22px; height: 22px; border-radius: 50%;
    background: currentColor;
  }
  .brand-name {
    font-family: 'Montserrat', sans-serif;
    font-weight: 700;
    text-transform: uppercase;
    letter-spacing: 1px;
  }
  .card-front .brand-name { font-size: 46px; }
  .front-url {
    font-family: 'Lato', sans-serif;
    font-size: 17px;
    letter-spacing: 7px;
  }
  /* Back */
  .card-back {
    background: var(--paper);
    display: flex;
    align-items: center;
  }
  .back-brand {
    width: 340px;
    display: flex;
    justify-content: center;
    color: var(--brand-blue);
  }
  .card-back .brand-name { font-size: 26px; }
  .card-back .brand-dot { width: 14px; height: 14px; }
  .divider {
    width: 1.5px;
    height: 190px;
    background: var(--rule-blue);
  }
  .contact {
    padding-left: 34px;
    color: var(--text-grey);
  }
  .person-name {
    font-family: 'Montserrat', sans-serif;
    font-weight: 700;
    font-size: 28px;
    color: var(--brand-blue);
    text-transform: uppercase;
  }
  .person-title {
    font-size: 14.5px;
    margin: 4px 0 20px;
  }
  .contact-list { list-style: none; }
  .contact-list li {
    display: flex;
    align-items: center;
    gap: 12px;
    font-size: 15px;
    line-height: 27px;
  }
  .contact-list svg { width: 16px; height: 16px; fill: var(--brand-blue); flex: none; }
  .url-accent { color: var(--brand-blue); }
</style>
</head>
<body>
  <section class="card card-front">
    <div class="brand-lockup">
      <span class="brand-dot"></span>
      <span class="brand-name">Marlo Vitality</span>
    </div>
    <p class="front-url">www.marlovitality.example</p>
  </section>

  <section class="card card-back">
    <div class="back-brand">
      <div class="brand-lockup">
        <span class="brand-dot"></span>
        <span class="brand-name">Marlo Vitality</span>
      </div>
    </div>
    <div class="divider"></div>
    <div class="contact">
      <h1 class="person-name">Tomás Arribal</h1>
      <p class="person-title">Wellness Coach, Consultant &amp; Trainer</p>
      <ul class="contact-list">
        <li>
          <svg viewBox="0 0 24 24" aria-hidden="true"><path d="M6.6 10.8a15.1 15.1 0 006.6 6.6l2.2-2.2c.3-.3.7-.4 1-.2 1.1.4 2.3.6 3.6.6.6 0 1 .4 1 1V20c0 .6-.4 1-1 1C10.6 21 3 13.4 3 4c0-.6.4-1 1-1h3.5c.6 0 1 .4 1 1 0 1.3.2 2.5.6 3.6.1.3 0 .7-.2 1z"/></svg>
          (+34) 612 480 397 (Spain)
        </li>
        <li>
          <svg viewBox="0 0 24 24" aria-hidden="true"><path d="M6.6 10.8a15.1 15.1 0 006.6 6.6l2.2-2.2c.3-.3.7-.4 1-.2 1.1.4 2.3.6 3.6.6.6 0 1 .4 1 1V20c0 .6-.4 1-1 1C10.6 21 3 13.4 3 4c0-.6.4-1 1-1h3.5c.6 0 1 .4 1 1 0 1.3.2 2.5.6 3.6.1.3 0 .7-.2 1z"/></svg>
          +1 (555) 318 2046 (USA)
        </li>
        <li>
          <svg viewBox="0 0 24 24" aria-hidden="true"><path d="M2 5h20v14H2z M4 7v.5l8 5 8-5V7l-8 5z" fill-rule="evenodd"/></svg>
          info@marlovitality.example
        </li>
        <li>
          <svg viewBox="0 0 24 24" aria-hidden="true"><path d="M12 2a10 10 0 100 20 10 10 0 000-20zm0 2c.9 1.2 1.6 2.6 2 4h-4c.4-1.4 1.1-2.8 2-4zM4.3 14a8 8 0 010-4h3.4a16 16 0 000 4zm.8 2h3c.3 1.3.8 2.5 1.5 3.6A8 8 0 015.1 16zM8.1 8h-3a8 8 0 014.5-3.6C8.9 5.5 8.4 6.7 8.1 8zM12 20c-.9-1.2-1.6-2.6-2-4h4c-.4 1.4-1.1 2.8-2 4zm2.3-6H9.7a14 14 0 010-4h4.6a14 14 0 010 4zm.1 5.6c.7-1.1 1.2-2.3 1.5-3.6h3a8 8 0 01-4.5 3.6zM16.3 14a16 16 0 000-4h3.4a8 8 0 010 4zm-.4-6c-.3-1.3-.8-2.5-1.5-3.6A8 8 0 0118.9 8z"/></svg>
          <span>www.<span class="url-accent">marlovitality</span>.example</span>
        </li>
      </ul>
    </div>
  </section>
</body>
</html>
```